Corporate ppt for clients and partners /knowledge in German is important

We need to better design our ppt's that are used to present our firm to clients. Attached is the version that we currently use to explain our services to potential clients.
I would like to see a design that communicates clarity, integrity and uniqueness.

```html
<!DOCTYPE html>
<html lang="de">
<head>
<meta charset="utf-8">
<title>Wer wir sind – Nordlicht Security</title>
<link rel="stylesheet" href="https://fonts.googleapis.com/css2?family=Ubuntu:wght@400;500;700&display=swap">
<style>
  :root {
    --brand-blue: #0b4f9e;
    --heading-blue: #0e57a8;
    --hero-light: #8fd0f5;
    --hero-mid: #3f9ee0;
    --hero-deep: #1267bd;
    --text-dark: #2b2b2b;
    --white: #ffffff;
    --accent-blue: #1c86d6;
  }
  html, body {
    margin: 0;
    padding: 0;
    overflow: hidden;
    background: var(--white);
  }
  .slide {
    position: relative;
    width: 1200px;
    height: 900px;
    overflow: hidden;
    background: var(--white);
    font-family: "Ubuntu", sans-serif;
  }
  .hero-visual {
    position: absolute;
    left: 0;
    top: 0;
    width: 1200px;
    height: 268px;
    background:
      radial-gradient(ellipse 420px 240px at 720px 120px, rgba(255,255,255,0.55), rgba(255,255,255,0) 70%),
      linear-gradient(100deg, var(--hero-light) 0%, var(--hero-mid) 35%, var(--hero-light) 60%, var(--hero-deep) 100%);
  }
  .hero-divider {
    position: absolute;
    left: 0;
    top: 262px;
    width: 1200px;
    height: 50px;
  }
  .content {
    position: absolute;
    left: 46px;
    top: 340px;
    width: 1140px;
  }
  .section-title {
    margin: 0 0 20px;
    font-size: 27px;
    font-weight: 500;
    color: var(--heading-blue);
    letter-spacing: 0.2px;
  }
  .body-copy {
    margin: 0 0 30px;
    font-size: 21px;
    line-height: 30px;
    color: var(--text-dark);
    white-space: nowrap;
  }
  .footer-bar {
    position: absolute;
    left: 0;
    bottom: 0;
    width: 1200px;
    height: 36px;
    background: var(--brand-blue);
  }
  .copyright {
    position: absolute;
    left: 10px;
    top: 7px;
    font-size: 17px;
    font-weight: 500;
    color: var(--white);
  }
  .corner-tab {
    position: absolute;
    left: 1106px;
    top: 852px;
    width: 84px;
    height: 48px;
  }
</style>
</head>
<body>
<main class="slide">
  <div class="hero-visual" role="img" aria-label="Hand berührt ein leuchtendes digitales Netzwerk aus verbundenen Kreisen auf blauem Hintergrund"></div>

  <svg class="hero-divider" viewBox="0 0 1200 50" aria-hidden="true">
    <path d="M0 4 H118 C140 4 156 14 168 46 C180 14 196 4 218 4 H1200 V10 H222 C200 10 186 20 168 50 C150 20 136 10 114 10 H0 Z" fill="var(--brand-blue)"/>
  </svg>

  <section class="content">
    <h1 class="section-title">WER WIR SIND</h1>
    <p class="body-copy">Nordlicht Security ist ein führendes Unternehmen auf dem Gebiet umfassender Sicherheitsanalysen und<br>zielgerichteter Penetration Tests</p>
    <p class="body-copy">Wir bieten Ihnen qualitativ hochwertige und umfassende Penetration Tests im gesamten IT-Umfeld. Unsere<br>icherheitsanalysten sind allesamt renommierte Experten mit dem entsprechenden Wissen sowie der nötigen Erfahrung<br>bei manuellem Vorgehen und helfen Ihnen Ihre kritische IT-Infrastruktur, mögliche Web-Applikationen, eigene</p>
    <p class="body-copy">Software-Programmierung oder auch das Sicherheitsbewusstsein Ihrer Mitarbeiter stark zu verbessern. Unsere<br>permanenten Recherchen und Entwicklungen im eigenen Forschungslabor geben uns, gegenüber der wachsenden<br>Cyber-Kriminalität, einen entscheidenden</p>
    <p class="body-copy">Wissensvorsprung. Diese Pionierarbeit können wir Ihnen auch in Form von individuellen Workshops und Schulungen<br>gerne weiter vermitteln. Generell wahren wir durch unsere Fokussierung auf Penetration Tests die nötige Neutralität<br>und Objektivität und stellen die gewünschte &nbsp;nbefang enheit unserer &nbsp;Ergebnisse sowie Empfehlungen sicher.</p>
  </section>

  <footer class="footer-bar">
    <span class="copyright">Copyright text here</span>
  </footer>

  <svg class="corner-tab" viewBox="0 0 84 48" aria-hidden="true">
    <rect x="4" y="0" width="76" height="48" rx="14" fill="var(--white)"/>
    <circle cx="42" cy="22" r="12" fill="var(--accent-blue)"/>
  </svg>
</main>
</body>
</html>
```